Major Event Flyer

We need an A4 flyer to promote the Wexley Plate greyhound event.
I have included the poster from last year as an example.
We will need the Wexley Logo, HTM Logo and Punterly logos included in the design. Greyhound Racing images can be supplied on request.
Here is the info for the poster:
Punterly Wexley Plate @ Hollisford
Thursday 24 October
Gates Open 6pm
Venue – Hollisford Greyhound Racing Club, Marlow Rd, Springvale
Competitions and Giveaways
Special Guests
Live Music and Entertainment
Club Details: Ph (03) 5871 4620
www.wexleychasers.com.au

```html
<!DOCTYPE html>
<html lang="en">
<head>
<meta charset="utf-8">
<title>Punterly Wexley Plate – Event Flyer</title>
<link rel="stylesheet" href="https://fonts.googleapis.com/css2?family=Audiowide&family=Exo+2:ital,wght@0,700;1,900&family=Kaushan+Script&family=Orbitron:wght@600;800&display=swap">
<style>
  :root{
    --page:#ffffff;
    --ink:#1b1d1f;
    --ink-deep:#0f1112;
    --white:#ffffff;
    --green:#12b548;
    --green-bright:#19d45a;
    --orange:#f7941d;
    --yellow:#f9c11a;
    --blue:#2f5bff;
    --blue-light:#4aa8ff;
    --navy:#1a2340;
    --pale:#e6f1fb;
  }
  *{box-sizing:border-box;margin:0;padding:0}
  html,body{width:1200px;height:1200px;overflow:hidden;background:var(--page)}
  .flyer{position:absolute;left:245px;top:100px;width:710px;height:1006px;background:var(--ink);overflow:hidden;font-family:"Audiowide",sans-serif;color:var(--white)}
  .abs{position:absolute}
  .decor{position:absolute;left:0;top:0;width:710px;height:1006px;pointer-events:none}

  /* header */
  .title-year{left:26px;top:18px;font-size:64px;letter-spacing:8px;color:var(--white)}
  .title-name{left:24px;top:76px;font-size:52px;font-style:italic;color:var(--white);letter-spacing:1px}
  .title-script{left:200px;top:118px;font-family:"Kaushan Script",cursive;font-size:42px;color:var(--green)}
  .date-day{left:414px;top:20px;font-family:"Orbitron",sans-serif;font-weight:800;font-size:17px;color:var(--yellow);letter-spacing:1px}
  .date-num{right:22px;top:-4px;font-family:"Orbitron",sans-serif;font-weight:800;font-size:84px;line-height:1;
    background:linear-gradient(180deg,var(--blue-light),var(--blue));-webkit-background-clip:text;background-clip:text;color:transparent}
  .date-month{right:20px;top:78px;font-family:"Orbitron",sans-serif;font-weight:800;font-size:25px;color:var(--white);letter-spacing:1px}

  /* photo */
  .race-photo{left:0;top:172px;width:710px;height:470px;
    background:radial-gradient(ellipse at 50% 45%,#8a8f94 0%,#5d5650 35%,#3b3630 70%,#24221f 100%)}

  /* headline */
  .headline{left:0;width:710px;top:628px;text-align:center;font-family:"Exo 2",sans-serif;font-weight:900;font-style:italic;font-size:74px;letter-spacing:1px;
    background:linear-gradient(180deg,var(--blue-light),var(--blue));-webkit-background-clip:text;background-clip:text;color:transparent}
  .subhead{left:0;width:710px;top:700px;text-align:center;font-family:"Kaushan Script",cursive;font-size:46px;
    background:linear-gradient(90deg,var(--yellow),var(--orange));-webkit-background-clip:text;background-clip:text;color:transparent}

  .features{left:22px;top:768px;width:666px;height:36px;display:flex;align-items:center;justify-content:center;
    background:linear-gradient(90deg,var(--yellow),var(--green) 50%,var(--blue));font-size:18px;letter-spacing:1px;color:var(--white)}

  /* venue */
  .venue{left:0;top:804px;width:710px;height:76px;background:var(--pale)}
  .venue-label{left:48px;top:6px;font-family:"Kaushan Script",cursive;font-size:46px;
    background:linear-gradient(90deg,var(--blue),var(--green));-webkit-background-clip:text;background-clip:text;color:transparent}
  .venue-rule{left:224px;top:12px;width:2px;height:52px;background:var(--navy)}
  .venue-address{left:248px;top:18px;font-size:15px;line-height:20px;color:var(--navy);letter-spacing:.5px}

  /* gates */
  .sponsors{left:0;top:880px;width:710px;height:73px;background:var(--ink-deep)}
  .brand{top:22px;font-family:"Exo 2",sans-serif;font-weight:700;font-size:22px;color:var(--white)}
  .brand-htm{left:18px}
  .brand-punterly{left:104px}
  .brand-mark{left:84px;top:30px;width:14px;height:14px;background:var(--blue)}
  .gates{left:220px;top:14px;width:490px;height:46px;display:flex;align-items:center;padding-left:26px;
    background:linear-gradient(90deg,var(--yellow),var(--orange));font-family:"Orbitron",sans-serif;font-weight:800;font-size:27px;color:var(--ink-deep);letter-spacing:1px}
  .gates svg{margin-right:18px}

  /* footer */
  .footer{left:0;top:953px;width:710px;height:53px;background:var(--ink-deep)}
  .phone{left:0;top:0;width:214px;height:53px;background:var(--green);display:flex;align-items:center;padding-left:10px;font-size:16px;color:var(--white)}
  .phone-icon{width:24px;height:24px;background:var(--yellow);display:flex;align-items:center;justify-content:center;margin-right:14px}
  .web{left:238px;top:16px;font-size:18px;letter-spacing:1px;color:var(--white)}
</style>
</head>
<body>
<main class="flyer">
  <div class="abs race-photo" role="img" aria-label="Photograph of four greyhounds in racing jackets sprinting towards the camera on a dirt track"></div>

  <svg class="decor" viewBox="0 0 710 1006" aria-hidden="true">
    <rect x="0" y="0" width="710" height="172" fill="#1b1d1f"/>
    <path d="M352 0 Q420 120 710 150 L710 142 Q440 110 372 0 Z" fill="#f7941d"/>
    <path d="M0 540 Q300 690 710 560 L710 700 L0 700 Z" fill="#1b1d1f"/>
    <path d="M0 528 Q320 680 710 548 L710 600 Q330 720 0 610 Z" fill="#12b548"/>
    <line x1="24" y1="142" x2="190" y2="142" stroke="#12b548" stroke-width="2"/>
    <line x1="290" y1="142" x2="330" y2="142" stroke="#12b548" stroke-width="2"/>
    <line x1="600" y1="110" x2="690" y2="110" stroke="#2f5bff" stroke-width="2"/>
    <line x1="620" y1="116" x2="690" y2="116" stroke="#12b548" stroke-width="2"/>
    <line x1="500" y1="858" x2="700" y2="858" stroke="#12b548" stroke-width="2"/>
    <line x1="540" y1="865" x2="700" y2="865" stroke="#2f5bff" stroke-width="2"/>
  </svg>

  <div class="abs title-year">2024</div>
  <div class="abs title-name">Wexley</div>
  <div class="abs title-script">Plate</div>
  <div class="abs date-day">THURSDAY</div>
  <div class="abs date-num">24</div>
  <div class="abs date-month">OCTOBER</div>

  <h1 class="abs headline">COMPETITIONS</h1>
  <div class="abs subhead">&amp; Giveaways</div>
  <div class="abs features">★ SPECIAL GUESTS – LIVE MUSIC &amp; ENTERTAINMENT ★</div>

  <section class="abs venue">
    <div class="abs venue-label">Venue</div>
    <div class="abs venue-rule"></div>
    <address class="abs venue-address" style="font-style:normal">HOLLISFORD GREYHOUND RACING CLUB,<br>MARLOW RD, SPRINGVALE</address>
  </section>

  <section class="abs sponsors">
    <div class="abs brand brand-htm">HTM</div>
    <div class="abs brand-mark"></div>
    <div class="abs brand brand-punterly">Punterly</div>
    <div class="abs gates">
      <svg width="50" height="20" viewBox="0 0 50 20" aria-hidden="true"><path d="M0 0L10 10L0 20ZM18 0L28 10L18 20ZM36 0L46 10L36 20Z" fill="#0f1112"/></svg>
      GATES OPEN 6PM
    </div>
  </section>

  <footer class="abs footer">
    <div class="abs phone">
      <span class="phone-icon"><svg width="14" height="14" viewBox="0 0 24 24" aria-hidden="true"><path d="M6.6 10.8a15 15 0 0 0 6.6 6.6l2.2-2.2a1 1 0 0 1 1-.25 11.4 11.4 0 0 0 3.6.57 1 1 0 0 1 1 1V20a1 1 0 0 1-1 1A17 17 0 0 1 3 4a1 1 0 0 1 1-1h3.5a1 1 0 0 1 1 1c0 1.25.2 2.45.57 3.57a1 1 0 0 1-.25 1z" fill="#1b1d1f"/></svg></span>
      (03) 5871 4620
    </div>
    <div class="abs web">WWW.WEXLEYCHASERS.COM.AU</div>
  </footer>
</main>
</body>
</html>
```